dorwial business card design so that it looks better

need a new business card designed. use our website, dorwian.com for example. I attached an example of a previous card we had and liked. this is for law enforcement and we have attached a previous business card as an example. This site forces me to select color and font, ignore those as I picked stuff just to get this completed.

Target Market(s)

law enforcement, local government

Contact Information for Business Card

see the attached example and our website

Font styles to use
Serif

```html
<!DOCTYPE html>
<html lang="en">
<head>
<meta charset="utf-8">
<title>Dorwial Business Card</title>
<link rel="stylesheet" href="https://fonts.googleapis.com/css2?family=Arimo:wght@400;700&display=swap">
<style>
  :root {
    --navy: #071a26;
    --blue: #1a75bf;
    --ink: #111417;
    --paper: #ffffff;
    --backdrop: #e9e9ea;
  }
  * { margin: 0; padding: 0; box-sizing: border-box; }
  html, body {
    width: 1200px; height: 902px; overflow: hidden;
    background: var(--backdrop);
    font-family: "Arimo", Arial, sans-serif;
  }
  .card {
    position: absolute; left: 80px; top: 155px;
    width: 1040px; height: 592px;
    background: var(--navy);
    overflow: hidden;
    box-shadow: 0 6px 24px rgba(0,0,0,0.18);
  }
  .card-shapes { position: absolute; inset: 0; width: 100%; height: 100%; }
  .brand-name {
    position: absolute; left: 58px; top: 84px;
    font-weight: 700; font-size: 104px; line-height: 1;
    letter-spacing: 4px; color: var(--navy);
  }
  .person { position: absolute; left: 58px; top: 290px; }
  .person-name {
    font-weight: 700; font-size: 35px; line-height: 1.05;
    color: var(--navy); letter-spacing: 0.5px;
  }
  .person-title { font-size: 26px; color: var(--blue); line-height: 1.2; }
  .address {
    position: absolute; left: 58px; top: 370px;
    font-size: 26px; line-height: 33px; color: var(--ink); font-style: normal;
  }
  .contact-list {
    position: absolute; left: 58px; top: 455px; list-style: none;
    font-size: 26px; color: var(--ink);
  }
  .contact-item { display: flex; align-items: center; height: 32px; }
  .contact-icon { width: 22px; height: 22px; margin-right: 16px; fill: var(--blue); }
  .contact-web { letter-spacing: 2px; }
</style>
</head>
<body>
  <div class="card">
    <svg class="card-shapes" viewBox="0 0 940 535" preserveAspectRatio="none" aria-hidden="true">
      <path d="M600,0 L752,0 C795,90 832,190 838,278 C805,160 720,55 600,0 Z" fill="var(--blue)"/>
      <path d="M752,0 C795,90 832,190 838,278" fill="none" stroke="var(--paper)" stroke-width="4"/>
      <path d="M0,0 L600,0 C760,60 842,190 838,285 C834,380 800,465 755,535 L0,535 Z" fill="var(--paper)"/>
    </svg>

    <div class="brand-name">DORWIAL</div>

    <div class="person">
      <div class="person-name">ALAN REED</div>
      <div class="person-title">Director</div>
    </div>

    <address class="address">
      4120 Ashgrove Lane<br>
      Austin, TX 78704
    </address>

    <ul class="contact-list">
      <li class="contact-item">
        <svg class="contact-icon" viewBox="0 0 24 24"><path d="M6.6 2.5l3 4.2-2 1.8c1 2.8 3 5.6 5.4 7.4l1.9-1.8 4.2 3-1.8 3.6C10 20 3.5 12 4 4.2z"/></svg>
        866.555.0142
      </li>
      <li class="contact-item">
        <svg class="contact-icon" viewBox="0 0 24 24"><path d="M2 5h20v14H2z M4 7v.3l8 6 8-6V7z" fill-rule="evenodd"/></svg>
        info@dorwian.com
      </li>
      <li class="contact-item contact-web">
        <svg class="contact-icon" viewBox="0 0 24 24"><circle cx="12" cy="12" r="10"/><path d="M2 12h20M12 2c-3.5 3-3.5 17 0 20M12 2c3.5 3 3.5 17 0 20M4 7h16M4 17h16" stroke="#fff" stroke-width="1.2" fill="none"/></svg>
        www.dorwian.com
      </li>
    </ul>
  </div>
</body>
</html>
```